Meadowlark Learning Growth Partners (MLGP)

This is a professional business card. Logo and picture are a must on the front of the card. I am an educational consultant. I have been consulting for the past three years for a company. I am now opening my own company. My goal for my consulting company is to eventually consult all over America.

Target Market(s)

Educators, schools, professionals

Industry/Entity Type

Consulting

Contact Information for Business Card

Picture/logo on front, simple modern design

Font styles to use
Serif

Colors
85abd2
0355a3
3176b5
cedeed

Requirements
Must have
• picture, logo,
• Odessa Pruitt, Ed.S
• address 5073 Cormorant ridge Dr. Nashville, TN 37940
• Cell:616-555-0148
• Office: 629-555-0172
• www.Mlgpedu.example
• pruittodessa@mailbox.example

```html
<!DOCTYPE html>
<html lang="en">
<head>
<meta charset="utf-8">
<title>Meadowlark Learning Growth Partners – Business Card</title>
<link rel="stylesheet" href="https://fonts.googleapis.com/css2?family=Tinos:wght@400;700&display=swap">
<style>
  :root {
    --navy: #08418f;
    --navy-deep: #073a82;
    --stripe: #3176b5;
    --sky: #85abd2;
    --mist: #cedeed;
    --white: #ffffff;
    --ink: #0b3f8a;
    --page: #e6e8ec;
  }
  * { box-sizing: border-box; margin: 0; padding: 0; }
  html, body { width: 1200px; height: 1200px; overflow: hidden; }
  body {
    background: var(--page);
    font-family: "Tinos", "Times New Roman", serif;
    position: relative;
  }
  .card {
    position: absolute;
    left: 150px;
    width: 900px;
    height: 520px;
    overflow: hidden;
    box-shadow: 0 6px 18px rgba(0,0,0,0.18);
  }
  .card--front { top: 50px; background: var(--white); }
  .card--back { top: 620px; background: var(--navy-deep); }

  .front-bg { position: absolute; inset: 0; }

  .brand {
    position: absolute;
    display: flex;
    align-items: center;
  }
  .brand__mark {
    font-weight: 700;
    letter-spacing: 2px;
    display: flex;
    align-items: center;
    gap: 10px;
  }
  .brand__square { display: block; }
  .brand__rule { width: 2px; align-self: stretch; }
  .brand__name { font-weight: 700; line-height: 1.15; }

  .card--front .brand { left: 40px; top: 38px; height: 120px; color: var(--ink); }
  .card--front .brand__mark { font-size: 38px; width: 170px; }
  .card--front .brand__square { width: 16px; height: 16px; background: var(--ink); }
  .card--front .brand__rule { background: var(--ink); margin: 0 16px 0 6px; }
  .card--front .brand__name { font-size: 25px; }

  .holder {
    position: absolute;
    right: 30px;
    top: 70px;
    width: 400px;
    text-align: right;
    color: var(--white);
  }
  .holder__name { font-size: 31px; letter-spacing: 0.5px; }
  .holder__title { font-size: 25px; margin-top: 6px; }
  .holder__rule { height: 1.5px; background: var(--white); margin-top: 8px; opacity: 0.9; }

  .portrait {
    position: absolute;
    right: 0;
    bottom: 0;
    width: 270px;
    height: 330px;
    background: linear-gradient(180deg, #2e5d9e 0%, #c9b59a 45%, #1e2330 100%);
  }

  .contact {
    position: absolute;
    left: 40px;
    top: 280px;
    list-style: none;
    color: var(--ink);
    font-size: 21px;
  }
  .contact__item {
    display: flex;
    align-items: flex-start;
    gap: 16px;
    margin-bottom: 14px;
    line-height: 1.25;
  }
  .contact__icon { flex: none; width: 24px; height: 24px; margin-top: 1px; }

  .card--back .brand {
    left: 0; right: 0; top: 175px; height: 140px;
    justify-content: center;
    color: var(--white);
  }
  .card--back .brand__mark { font-size: 44px; }
  .card--back .brand__square { width: 18px; height: 18px; background: var(--white); }
  .card--back .brand__rule { background: var(--white); margin: 0 22px; }
  .card--back .brand__name { font-size: 30px; }

  .back-url {
    position: absolute;
    right: 46px;
    bottom: 42px;
    color: var(--white);
    font-size: 20px;
    letter-spacing: 0.5px;
  }
</style>
</head>
<body>

<section class="card card--front" aria-label="Business card front">
  <svg class="front-bg" width="900" height="520" viewBox="0 0 900 520" aria-hidden="true">
    <polygon points="455,0 900,0 900,520 682,520" fill="var(--stripe)"/>
    <polygon points="485,0 900,0 900,520 706,520" fill="var(--navy)"/>
  </svg>

  <div class="brand">
    <div class="brand__mark"><span class="brand__square"></span>MLGP</div>
    <span class="brand__rule"></span>
    <div class="brand__name">Meadowlark<br>Learning<br>Growth<br>Partners</div>
  </div>

  <div class="holder">
    <div class="holder__name">ODESSA PRUITT</div>
    <div class="holder__title">ED.S</div>
    <div class="holder__rule"></div>
  </div>

  <div class="portrait" role="img" aria-label="Portrait photograph of Odessa Pruitt"></div>

  <ul class="contact">
    <li class="contact__item">
      <svg class="contact__icon" viewBox="0 0 24 24" aria-hidden="true"><circle cx="12" cy="12" r="11" fill="none" stroke="var(--sky)" stroke-width="1.4"/><path d="M12 6.5a3.6 3.6 0 0 0-3.6 3.6c0 2.7 3.6 7 3.6 7s3.6-4.3 3.6-7A3.6 3.6 0 0 0 12 6.5z" fill="none" stroke="var(--ink)" stroke-width="1.4"/><circle cx="12" cy="10.1" r="1.2" fill="var(--ink)"/></svg>
      <span>5073 CORMORANT RIDGE DR. NASHVILLE,<br>TN 37940</span>
    </li>
    <li class="contact__item">
      <svg class="contact__icon" viewBox="0 0 24 24" aria-hidden="true"><circle cx="12" cy="12" r="11" fill="none" stroke="var(--sky)" stroke-width="1.4"/><path d="M8.3 6.8l2 2-1.2 1.6c.8 1.7 2 2.9 3.7 3.7l1.6-1.2 2 2-1.5 1.7c-3.8-.6-7-3.8-7.6-7.6z" fill="none" stroke="var(--ink)" stroke-width="1.4" stroke-linejoin="round"/></svg>
      <span>616-555-0148</span>
    </li>
    <li class="contact__item">
      <svg class="contact__icon" viewBox="0 0 24 24" aria-hidden="true"><circle cx="12" cy="12" r="11" fill="none" stroke="var(--sky)" stroke-width="1.4"/><path d="M8.3 6.8l2 2-1.2 1.6c.8 1.7 2 2.9 3.7 3.7l1.6-1.2 2 2-1.5 1.7c-3.8-.6-7-3.8-7.6-7.6z" fill="none" stroke="var(--ink)" stroke-width="1.4" stroke-linejoin="round"/></svg>
      <span>629-555-0172</span>
    </li>
    <li class="contact__item">
      <svg class="contact__icon" viewBox="0 0 24 24" aria-hidden="true"><circle cx="12" cy="12" r="11" fill="none" stroke="var(--sky)" stroke-width="1.4"/><circle cx="12" cy="12" r="6" fill="none" stroke="var(--ink)" stroke-width="1.3"/><ellipse cx="12" cy="12" rx="2.6" ry="6" fill="none" stroke="var(--ink)" stroke-width="1.1"/><line x1="6" y1="12" x2="18" y2="12" stroke="var(--ink)" stroke-width="1.1"/></svg>
      <span>WWW.MLGPEDU.EXAMPLE</span>
    </li>
    <li class="contact__item">
      <svg class="contact__icon" viewBox="0 0 24 24" aria-hidden="true"><circle cx="12" cy="12" r="11" fill="none" stroke="var(--sky)" stroke-width="1.4"/><rect x="6.5" y="8" width="11" height="8" fill="none" stroke="var(--ink)" stroke-width="1.3"/><path d="M6.5 8l5.5 4.5L17.5 8" fill="none" stroke="var(--ink)" stroke-width="1.3"/></svg>
      <span>PRUITTODESSA@MAILBOX.EXAMPLE</span>
    </li>
  </ul>
</section>

<section class="card card--back" aria-label="Business card back">
  <div class="brand">
    <div class="brand__mark"><span class="brand__square"></span>MLGP</div>
    <span class="brand__rule"></span>
    <div class="brand__name">Meadowlark<br>Learning<br>Growth<br>Partners</div>
  </div>
  <div class="back-url">WWW.MLGPEDU.EXAMPLE</div>
</section>

</body>
</html>
```